Poster for Wobble Evening - a weekly comedy/variety show

We would like a poster/postcard design for a weekly alternative comedy/variety show called Wobble Evening.
Style: The poster should be fun and eye catching and very bold. It should have an alternative feel, not mainstream. Weird, strange, bizarre and funny is good. The show's title "Wobble Evening" should be very prominent. I like the idea of it being busy and cartoony, a collage of weirdness. Fenwick Dabble's Spinning Carnival or Cpt. Quimby's Restless Ankle's Parade Troupe or psychedelic rock posters of the 70's.
Design Specifics: We are looking for one design that can both be on an 11" x 17" poster and reduced to a 4" x 6" postcard.
The copy:
-
vtm productions presents:
Wobble Evening
standup, music, storytelling, sketch and improv
Wednesdays @ Gullfeather Theatre
5164 W. Larkmont - 2nd Floor
Chicago, IL 60588
7:30 - The Loose Hour
8:30 - The Medley Hour
9:45 - Torbeck Ladder
Pay what you want
website: wobbleevening.example
-
The back of the postcard can be very simple. We may add stickers to it regularly with the specific dates and the names of guest performers.
UPDATE: I've updated the copy a little bit and made this a guaranteed contest.
Reason: I asked a couple designers to submit changes and have extended the deadline so that they have time to do that.
I have picked a design and I'm just now going to try to choose between the variations of that poster that the designer posted. No need to add any more designs unless I request them directly.
Young adults (20s-40s), college students, living on the north side of Chicago who are looking for a fun, inexpensive, cool night out during the week.
Club

```html
<!DOCTYPE html>
<html lang="en">
<head>
<meta charset="utf-8">
<title>Wobble Evening</title>
<link rel="stylesheet" href="https://fonts.googleapis.com/css2?family=Varela+Round&family=Playfair+Display:wght@900&family=Patrick+Hand+SC&family=Shadows+Into+Light+Two&family=Amatic+SC:wght@700&display=swap">
<style>
  :root {
    --ink: #2f2f33;
    --panel: rgba(236, 236, 242, 0.78);
    --panel-solid: #ececf1;
    --banner: #f7f7f5;
    --banner-shade: #b9b9bd;
    --navy: #26305e;
    --teal: #3f7f8f;
    --mint: #8fd0b0;
    --plum: #5a2d4c;
    --sky: #9cc7d8;
  }
  * { margin: 0; padding: 0; box-sizing: border-box; }
  html, body { width: 800px; height: 1200px; overflow: hidden; }
  body { position: relative; color: var(--ink); }

  .backdrop {
    position: absolute; inset: 0;
    background:
      radial-gradient(ellipse 60% 30% at 30% 35%, rgba(143,208,176,0.7), transparent 70%),
      radial-gradient(ellipse 50% 25% at 80% 70%, rgba(156,199,216,0.6), transparent 70%),
      linear-gradient(180deg, var(--navy) 0%, var(--teal) 30%, var(--mint) 48%, var(--teal) 68%, var(--sky) 80%, var(--plum) 100%);
  }

  .pill {
    position: absolute;
    background: var(--panel);
    border-radius: 40px;
    display: flex; align-items: center; justify-content: center;
    white-space: nowrap;
  }

  .presenter {
    left: 194px; top: 39px; width: 403px; height: 55px;
    font-family: "Varela Round", sans-serif; font-size: 30px;
  }
  .bubble { position: absolute; top: 56px; width: 125px; height: 76px; }
  .bubble--left { left: 42px; }
  .bubble--right { right: 42px; transform: scaleX(-1); }

  .ribbon { position: absolute; left: 0; top: 132px; width: 800px; height: 201px; }
  .title {
    position: absolute; left: 80px; top: 156px; width: 642px; height: 101px;
    display: flex; align-items: center; justify-content: center;
    font-family: "Playfair Display", serif; font-weight: 900;
    font-size: 60px; letter-spacing: 2px; text-transform: uppercase;
    color: var(--ink); white-space: nowrap;
    text-shadow: 3px 3px 0 var(--banner-shade);
  }

  .genres {
    left: 14px; top: 347px; width: 778px; height: 67px;
    font-family: "Patrick Hand SC", cursive; font-size: 31px;
    text-transform: uppercase; letter-spacing: 0.5px;
  }

  .venue {
    position: absolute; left: 115px; top: 444px; width: 570px; height: 226px;
    background: var(--panel); border-radius: 30px;
    font-family: "Shadows Into Light Two", cursive; font-style: normal;
    font-size: 34px; line-height: 60px;
    text-align: center; padding-top: 15px; white-space: nowrap;
  }

  .schedule {
    position: absolute; left: 153px; top: 715px; width: 528px; height: 313px;
    background: var(--panel); border-radius: 36px;
    padding: 18px 0 0 40px;
  }
  .slot { display: flex; align-items: center; height: 95px; white-space: nowrap; }
  .clock {
    width: 58px; height: 58px; border-radius: 50%;
    border: 4px solid var(--ink); background: var(--panel-solid);
    display: flex; align-items: center; justify-content: center;
    font-family: "Varela Round", sans-serif; font-size: 15px; font-weight: bold;
    margin-right: 20px; position: relative; flex: none;
  }
  .clock::before {
    content: ""; position: absolute; top: -10px; left: 50%;
    width: 10px; height: 6px; margin-left: -5px; background: var(--ink); border-radius: 2px;
  }
  .slot-name { font-family: "Amatic SC", cursive; font-size: 60px; }

  .dots { position: absolute; left: 360px; top: 1046px; width: 80px; height: 20px; }

  .price {
    left: 83px; top: 1076px; width: 639px; height: 70px;
    font-family: "Patrick Hand SC", cursive; font-size: 36px; letter-spacing: 2px;
    text-transform: uppercase;
  }
  .price-mark { position: absolute; top: 14px; width: 70px; height: 42px; background: var(--banner-shade); border-radius: 4px; }
  .price-mark--left { left: 28px; }
  .price-mark--right { right: 28px; }

  .website {
    left: 180px; top: 1152px; width: 440px; height: 48px;
    border-radius: 30px 30px 0 0;
    font-family: "Varela Round", sans-serif; font-size: 22px;
  }
</style>
</head>
<body>
  <div class="backdrop" role="img" aria-label="Marbled psychedelic texture in navy, teal, mint and plum"></div>

  <svg class="bubble bubble--left" viewBox="0 0 125 76" aria-hidden="true">
    <path d="M62 4 C100 4 121 22 121 40 C121 60 100 72 62 72 C30 72 4 56 4 38 C4 20 30 4 62 4 Z" fill="rgba(236,236,242,0.78)"/>
  </svg>
  <div class="pill presenter">vtm productions presents</div>
  <svg class="bubble bubble--right" viewBox="0 0 125 76" aria-hidden="true">
    <path d="M62 4 C100 4 121 22 121 40 C121 60 100 72 62 72 C30 72 4 56 4 38 C4 20 30 4 62 4 Z" fill="rgba(236,236,242,0.78)"/>
  </svg>

  <svg class="ribbon" viewBox="0 0 800 201" aria-hidden="true">
    <path d="M0 70 L110 70 L110 170 L0 170 L40 120 Z" fill="var(--banner)" stroke="var(--ink)" stroke-width="4"/>
    <path d="M800 70 L690 70 L690 170 L800 170 L760 120 Z" fill="var(--banner)" stroke="var(--ink)" stroke-width="4"/>
    <path d="M80 125 L110 170 L110 125 Z" fill="var(--banner-shade)" stroke="var(--ink)" stroke-width="3"/>
    <path d="M720 125 L690 170 L690 125 Z" fill="var(--banner-shade)" stroke="var(--ink)" stroke-width="3"/>
    <rect x="80" y="24" width="640" height="101" fill="var(--banner)" stroke="var(--ink)" stroke-width="5"/>
    <rect x="90" y="33" width="620" height="83" fill="none" stroke="var(--ink)" stroke-width="2"/>
  </svg>
  <h1 class="title">Wobble Evening</h1>

  <div class="pill genres">standup, music, storytelling, sketch and improv</div>

  <address class="venue">
    Wednesdays @ Gullfeather Theatre<br>
    5164 W. Larkmont - 2nd Floor<br>
    Chicago, IL 60588
  </address>

  <section class="schedule">
    <div class="slot"><span class="clock">7:30</span><span class="slot-name">The Loose Hour</span></div>
    <div class="slot"><span class="clock">8:30</span><span class="slot-name">The Medley Hour</span></div>
    <div class="slot"><span class="clock">9:45</span><span class="slot-name">Torbeck Ladder</span></div>
  </section>

  <svg class="dots" viewBox="0 0 80 20" aria-hidden="true">
    <circle cx="12" cy="10" r="5" fill="var(--panel-solid)"/>
    <circle cx="30" cy="10" r="7" fill="var(--panel-solid)"/>
    <circle cx="50" cy="10" r="7" fill="var(--panel-solid)"/>
    <circle cx="68" cy="10" r="5" fill="var(--panel-solid)"/>
  </svg>

  <div class="pill price">
    <span class="price-mark price-mark--left" role="img" aria-label="Cassette tape illustration"></span>
    Pay what you want
    <span class="price-mark price-mark--right" role="img" aria-label="Cassette tape illustration"></span>
  </div>

  <div class="pill website">website: wobbleevening.example</div>
</body>
</html>
```